QMCARGO FLYER

I would like a flyer to put out around town to advertise our business, (freight forwarding) i have a logo and i was also hoping we could have the reverse of the flyer in arabic, as alot of my clientele are from the Middle East. Photos could also be available?
Would like to have special offers to main destinations, i.e. Riyadh £2.50* All In
Jeddah £2.50* " "
Dubai""""""""""""""
Abu Dhabi"""""""""
Doha""""""""""""""
And some other major country (capitals) all the same price *subject to requirements

Airfreight / Sea freight
Airport Transport Services
Customs Clearance
Car Shipping
Packaging Material

contact details: Email: qmcargo@postvale.net
Tel: +44 (0) 20 7413 5961
Mob:+44 (0) 7392 816 054

Target Market(s)

Middle East
Arabic

Requirements
Must have
• Stand Out and be clear and not too cluttered.
• Want to get across exactly whats on offer.
• Reverse Mirrored in Arabic

```html
<!DOCTYPE html>
<html lang="en">
<head>
<meta charset="utf-8">
<title>QMCARGO Flyer</title>
<link href="https://fonts.googleapis.com/css2?family=PT+Sans+Narrow:wght@400;700&family=Open+Sans:wght@700&display=swap" rel="stylesheet">
<style>
  :root {
    --gold: #e2b100;
    --gold-soft: #c9a326;
    --ink: #1b1b1b;
    --paper: #f1f1f1;
    --paper-shade: #dedede;
    --tick: #2b6cb3;
    --stage: #d8d4cd;
    --photo-sky: #c9ccd0;
    --photo-ground: #8f8f8f;
  }
  * { margin: 0; padding: 0; box-sizing: border-box; }
  html, body { width: 1200px; height: 1000px; overflow: hidden; }
  body { background: var(--stage); position: relative; font-family: "PT Sans Narrow", sans-serif; color: var(--ink); }

  .flyer {
    position: absolute; left: 45px; top: 120px; width: 1110px; height: 760px;
    background: linear-gradient(135deg, #ffffff 0%, var(--paper) 55%, var(--paper-shade) 100%);
    overflow: hidden; box-shadow: 0 10px 30px rgba(0,0,0,.25);
  }
  .flyer-shapes { position: absolute; inset: 0; }

  .brand { position: absolute; left: 70px; top: 118px; display: flex; align-items: center; gap: 14px; }
  .brand-dot { width: 54px; height: 54px; border-radius: 50%; background: var(--ink); }
  .brand-name { font-weight: 700; font-size: 54px; line-height: 1; color: var(--ink); letter-spacing: 1px; }

  .banner {
    position: absolute; left: 0; background: var(--gold);
    font-weight: 700; color: var(--ink); text-transform: uppercase; line-height: 1;
    display: flex; align-items: center; padding-left: 50px; white-space: nowrap;
  }
  .banner--who { top: 262px; width: 420px; height: 62px; font-size: 50px; }
  .banner--offers { top: 528px; width: 420px; height: 60px; font-size: 50px; }

  .intro { position: absolute; left: 62px; top: 338px; font-size: 23px; line-height: 1.15; width: 420px; }

  .services { position: absolute; left: 66px; top: 396px; list-style: none; }
  .services li {
    font-family: "Open Sans", sans-serif; font-weight: 700; font-size: 16px; line-height: 21px;
    display: flex; align-items: center; gap: 9px; white-space: nowrap;
  }
  .services svg { width: 14px; height: 14px; flex: none; }

  .offers { position: absolute; top: 596px; font-weight: 700; font-size: 19px; line-height: 22px; border-collapse: collapse; }
  .offers--left { left: 62px; }
  .offers--right { left: 310px; }
  .offers td { white-space: nowrap; }
  .offers td:first-child { padding-right: 10px; }

  .tagline { position: absolute; left: 62px; top: 664px; font-size: 17px; }
  .footnote { position: absolute; right: 40px; top: 664px; font-family: "Open Sans", sans-serif; font-size: 11px; }

  .contact-band {
    position: absolute; left: 0; right: 0; bottom: 0; height: 70px; background: var(--gold);
    display: flex; align-items: center; justify-content: space-between; padding: 0 34px 0 58px;
    font-weight: 700; font-size: 23px; white-space: nowrap;
  }
  .contact-band .email { font-size: 28px; }
  .contact-item { display: flex; align-items: center; gap: 6px; }
  .contact-item svg { height: 26px; width: auto; }
</style>
</head>
<body>
<main class="flyer">
  <svg class="flyer-shapes" viewBox="0 0 1110 760">
    <defs>
      <linearGradient id="airfield" x1="0" y1="0" x2="0" y2="1">
        <stop offset="0" stop-color="#eef0f2"/>
        <stop offset=".35" stop-color="var(--photo-sky)"/>
        <stop offset=".55" stop-color="#a9a9a9"/>
        <stop offset="1" stop-color="var(--photo-ground)"/>
      </linearGradient>
      <linearGradient id="boxes" x1="0" y1="0" x2="1" y2="1">
        <stop offset="0" stop-color="#c99f6a"/>
        <stop offset="1" stop-color="#3b66b4"/>
      </linearGradient>
      <linearGradient id="van" x1="0" y1="0" x2="0" y2="1">
        <stop offset="0" stop-color="#b8a48a"/>
        <stop offset=".5" stop-color="#dcdcdc"/>
        <stop offset="1" stop-color="#6d6d6d"/>
      </linearGradient>
    </defs>
    <polygon points="360,280 405,280 585,0 545,0" fill="var(--gold)"/>
    <polygon points="400,150 590,70 590,110 400,168" fill="var(--gold-soft)"/>
    <circle cx="925" cy="175" r="445" fill="var(--gold)"/>
    <circle cx="925" cy="175" r="432" fill="url(#airfield)" role="img" aria-label="Photo: cargo aircraft being loaded on the apron with pallets and sports cars on loading dollies"/>
    <circle cx="565" cy="445" r="84" fill="var(--gold)"/>
    <circle cx="565" cy="445" r="72" fill="url(#boxes)" role="img" aria-label="Photo: stacked cardboard boxes and blue suitcases"/>
    <circle cx="800" cy="565" r="104" fill="var(--gold)"/>
    <circle cx="800" cy="565" r="91" fill="url(#van)" role="img" aria-label="Photo: company van parked near an aircraft at dusk"/>
  </svg>

  <div class="brand">
    <span class="brand-dot"></span>
    <span class="brand-name">QMCARGO</span>
  </div>

  <h2 class="banner banner--who">Who we are?</h2>
  <p class="intro">QM Cargo take pleasure to introduce ourselves as International Freight Forwarders Services:</p>

  <ul class="services">
    <li><svg viewBox="0 0 16 16"><path d="M1 9l4 4 10-11" fill="none" stroke="var(--tick)" stroke-width="3"/></svg>Airfreight / Sea freight</li>
    <li><svg viewBox="0 0 16 16"><path d="M1 9l4 4 10-11" fill="none" stroke="var(--tick)" stroke-width="3"/></svg>Airport Transport Services</li>
    <li><svg viewBox="0 0 16 16"><path d="M1 9l4 4 10-11" fill="none" stroke="var(--tick)" stroke-width="3"/></svg>Customs Clearance</li>
    <li><svg viewBox="0 0 16 16"><path d="M1 9l4 4 10-11" fill="none" stroke="var(--tick)" stroke-width="3"/></svg>Car Shipping</li>
    <li><svg viewBox="0 0 16 16"><path d="M1 9l4 4 10-11" fill="none" stroke="var(--tick)" stroke-width="3"/></svg>Packaging Material</li>
    <li><svg viewBox="0 0 16 16"><path d="M1 9l4 4 10-11" fill="none" stroke="var(--tick)" stroke-width="3"/></svg>Excess Baggage</li>
  </ul>

  <h2 class="banner banner--offers">Special offers</h2>

  <table class="offers offers--left">
    <tr><td>Riyadh</td><td>£2.50* All In</td></tr>
    <tr><td>Jeddah</td><td>£2.50* All in</td></tr>
    <tr><td>Dubai</td><td>£2.50* All in</td></tr>
  </table>
  <table class="offers offers--right">
    <tr><td>Abu Dhabi</td><td>£2.50* All in</td></tr>
    <tr><td>Doha</td><td>£2.50* All in</td></tr>
  </table>

  <p class="tagline">Middle-east cargo specialist</p>
  <p class="footnote">*subject to requirements</p>

  <footer class="contact-band">
    <span class="email">Email: qmcargo@postvale.net</span>
    <span class="contact-item">
      <svg viewBox="0 0 24 24"><path d="M6 2l4 5-2 3c1 3 3 5 6 6l3-2 5 4-3 4C10 22 2 14 2 5z" fill="var(--ink)"/></svg>
      +44 (0) 20 7413 5961
    </span>
    <span class="contact-item">
      <svg viewBox="0 0 16 26"><rect x="1.5" y="1.5" width="13" height="23" rx="2" fill="none" stroke="var(--ink)" stroke-width="2.5"/><circle cx="8" cy="21" r="1.3" fill="var(--ink)"/></svg>
      +44 (0) 7392 816 054
    </span>
    <span class="contact-item">
      <svg viewBox="0 0 26 24"><rect x="6" y="1" width="14" height="7" fill="var(--ink)"/><rect x="1" y="8" width="24" height="10" rx="2" fill="var(--ink)"/><rect x="6" y="15" width="14" height="8" fill="var(--ink)" stroke="var(--gold)" stroke-width="1.5"/></svg>
      +44 (0) 20 7413 5961
    </span>
  </footer>
</main>
</body>
</html>
```